Tolmira is a sparkling water from the Caucasian mountains.

Target Market(s)

High-end consumers

Colors

Designer to choose colors to be used in the design.

Requirements
Must have
• Sense of water from the mountines
Nice to have
• Sense of beign healing water

```html
<!DOCTYPE html>
<html lang="en">
<head>
<meta charset="utf-8">
<title>Tolmira Sparkling Water – Bottle Range</title>
<link rel="stylesheet" href="https://fonts.googleapis.com/css2?family=Playfair+Display:wght@400;700&family=Pinyon+Script&family=Roboto&display=swap">
<style>
  :root {
    --canvas: #f6f6f6;
    --glass: #ffffff;
    --aqua-tint: #47c2d8;  --aqua-ink: #1d6c84;
    --lime-tint: #7fd02c;  --lime-ink: #4d8714;
    --rose-tint: #e02f7f;  --rose-ink: #981a54;
    --violet-tint: #8b3fd8; --violet-ink: #4a1a8c;
    --azure-tint: #2f86d8; --azure-ink: #1a4f86;
  }
  * { margin: 0; padding: 0; box-sizing: border-box; }
  html, body { width: 1200px; height: 790px; overflow: hidden; background: var(--canvas); }
  .range { position: relative; width: 1200px; height: 790px; }
  .bottle { position: absolute; width: 160px; height: 632px; top: 108px; color: var(--ink); }
  .bottle--aqua   { left: 102px; --tint: var(--aqua-tint);   --ink: var(--aqua-ink); }
  .bottle--lime   { left: 300px; --tint: var(--lime-tint);   --ink: var(--lime-ink); }
  .bottle--rose   { left: 496px; top: 114px; --tint: var(--rose-tint);   --ink: var(--rose-ink); }
  .bottle--violet { left: 688px; top: 114px; --tint: var(--violet-tint); --ink: var(--violet-ink); }
  .bottle--azure  { left: 878px; top: 114px; --tint: var(--azure-tint);  --ink: var(--azure-ink); }
  .bottle__shape { position: absolute; inset: 0; width: 160px; height: 632px; }
  .bottle__label { position: absolute; left: 0; width: 160px; text-align: center; }
  .brand-name { top: 164px; font: 400 40px/1 "Playfair Display", serif; color: var(--ink); }
  .brand-tag { top: 208px; font: 400 8px/1 "Playfair Display", serif; letter-spacing: 0.06em; color: var(--ink); opacity: .8; }
  .headline { top: 442px; font: 700 25px/1.05 "Playfair Display", serif; color: var(--ink); }
  .origin { top: 512px; font: 400 15px/1 "Pinyon Script", cursive; color: var(--ink); opacity: .85; }
  .volume { top: 536px; font: 400 8.5px/1 "Roboto", sans-serif; color: #333; }
</style>
</head>
<body>
<main class="range">

  <article class="bottle bottle--aqua">
    <svg class="bottle__shape" viewBox="0 0 200 790" aria-hidden="false">
      <defs>
        <linearGradient id="glass-aqua" x1="0" y1="0" x2="0" y2="1">
          <stop offset="0" style="stop-color:var(--tint)"/>
          <stop offset=".35" style="stop-color:var(--tint);stop-opacity:.35"/>
          <stop offset=".62" style="stop-color:var(--glass)"/>
          <stop offset=".85" style="stop-color:var(--tint);stop-opacity:.3"/>
          <stop offset="1" style="stop-color:var(--tint)"/>
        </linearGradient>
        <linearGradient id="peak-aqua" x1="0" y1="0" x2="0" y2="1">
          <stop offset="0" style="stop-color:var(--tint);stop-opacity:0"/>
          <stop offset=".5" style="stop-color:var(--tint);stop-opacity:.8"/>
          <stop offset="1" style="stop-color:var(--tint);stop-opacity:.15"/>
        </linearGradient>
        <clipPath id="clip-aqua"><path d="M72,56 L72,80 C72,130 5,170 5,250 C5,320 22,350 22,400 C22,440 10,450 10,480 L10,730 C10,760 20,790 40,790 L160,790 C180,790 190,760 190,730 L190,480 C190,450 178,440 178,400 C178,350 195,320 195,250 C195,170 128,130 128,80 L128,56 Z"/></clipPath>
      </defs>
      <rect x="68" y="0" width="64" height="48" rx="5" style="fill:var(--tint)"/>
      <rect x="60" y="48" width="80" height="7" rx="3" style="fill:var(--tint)"/>
      <path d="M72,56 L72,80 C72,130 5,170 5,250 C5,320 22,350 22,400 C22,440 10,450 10,480 L10,730 C10,760 20,790 40,790 L160,790 C180,790 190,760 190,730 L190,480 C190,450 178,440 178,400 C178,350 195,320 195,250 C195,170 128,130 128,80 L128,56 Z" fill="url(#glass-aqua)"/>
      <g clip-path="url(#clip-aqua)" role="img" aria-label="Snow-capped mountain range">
        <rect x="0" y="320" width="200" height="150" fill="url(#peak-aqua)"/>
      </g>
    </svg>
    <div class="bottle__label brand-name">Tolmira</div>
    <div class="bottle__label brand-tag">SPARKLING WATER</div>
    <h2 class="bottle__label headline">SPARKLING<br>WATER</h2>
    <div class="bottle__label origin">Caucasian Mountains</div>
    <div class="bottle__label volume">16.9 fl oz (500 ml)</div>
  </article>

  <article class="bottle bottle--lime">
    <svg class="bottle__shape" viewBox="0 0 200 790">
      <defs>
        <linearGradient id="glass-lime" x1="0" y1="0" x2="0" y2="1">
          <stop offset="0" style="stop-color:var(--tint)"/>
          <stop offset=".35" style="stop-color:var(--tint);stop-opacity:.35"/>
          <stop offset=".62" style="stop-color:var(--glass)"/>
          <stop offset=".85" style="stop-color:var(--tint);stop-opacity:.3"/>
          <stop offset="1" style="stop-color:var(--tint)"/>
        </linearGradient>
        <linearGradient id="peak-lime" x1="0" y1="0" x2="0" y2="1">
          <stop offset="0" style="stop-color:var(--tint);stop-opacity:0"/>
          <stop offset=".5" style="stop-color:var(--tint);stop-opacity:.8"/>
          <stop offset="1" style="stop-color:var(--tint);stop-opacity:.15"/>
        </linearGradient>
        <clipPath id="clip-lime"><path d="M72,56 L72,80 C72,130 5,170 5,250 C5,320 22,350 22,400 C22,440 10,450 10,480 L10,730 C10,760 20,790 40,790 L160,790 C180,790 190,760 190,730 L190,480 C190,450 178,440 178,400 C178,350 195,320 195,250 C195,170 128,130 128,80 L128,56 Z"/></clipPath>
      </defs>
      <rect x="68" y="0" width="64" height="48" rx="5" style="fill:var(--tint)"/>
      <rect x="60" y="48" width="80" height="7" rx="3" style="fill:var(--tint)"/>
      <path d="M72,56 L72,80 C72,130 5,170 5,250 C5,320 22,350 22,400 C22,440 10,450 10,480 L10,730 C10,760 20,790 40,790 L160,790 C180,790 190,760 190,730 L190,480 C190,450 178,440 178,400 C178,350 195,320 195,250 C195,170 128,130 128,80 L128,56 Z" fill="url(#glass-lime)"/>
      <g clip-path="url(#clip-lime)" role="img" aria-label="Snow-capped mountain range">
        <rect x="0" y="320" width="200" height="150" fill="url(#peak-lime)"/>
      </g>
    </svg>
    <div class="bottle__label brand-name">Tolmira</div>
    <div class="bottle__label brand-tag">SPARKLING WATER</div>
    <h2 class="bottle__label headline">SPARKLING<br>WATER</h2>
    <div class="bottle__label origin">Caucasian Mountains</div>
    <div class="bottle__label volume">16.9 fl oz (500 ml)</div>
  </article>

  <article class="bottle bottle--rose">
    <svg class="bottle__shape" viewBox="0 0 200 790">
      <defs>
        <linearGradient id="glass-rose" x1="0" y1="0" x2="0" y2="1">
          <stop offset="0" style="stop-color:var(--tint)"/>
          <stop offset=".35" style="stop-color:var(--tint);stop-opacity:.35"/>
          <stop offset=".62" style="stop-color:var(--glass)"/>
          <stop offset=".85" style="stop-color:var(--tint);stop-opacity:.3"/>
          <stop offset="1" style="stop-color:var(--tint)"/>
        </linearGradient>
        <linearGradient id="peak-rose" x1="0" y1="0" x2="0" y2="1">
          <stop offset="0" style="stop-color:var(--tint);stop-opacity:0"/>
          <stop offset=".5" style="stop-color:var(--tint);stop-opacity:.8"/>
          <stop offset="1" style="stop-color:var(--tint);stop-opacity:.15"/>
        </linearGradient>
        <clipPath id="clip-rose"><path d="M72,56 L72,80 C72,130 5,170 5,250 C5,320 22,350 22,400 C22,440 10,450 10,480 L10,730 C10,760 20,790 40,790 L160,790 C180,790 190,760 190,730 L190,480 C190,450 178,440 178,400 C178,350 195,320 195,250 C195,170 128,130 128,80 L128,56 Z"/></clipPath>
      </defs>
      <rect x="68" y="0" width="64" height="48" rx="5" style="fill:var(--tint)"/>
      <rect x="60" y="48" width="80" height="7" rx="3" style="fill:var(--tint)"/>
      <path d="M72,56 L72,80 C72,130 5,170 5,250 C5,320 22,350 22,400 C22,440 10,450 10,480 L10,730 C10,760 20,790 40,790 L160,790 C180,790 190,760 190,730 L190,480 C190,450 178,440 178,400 C178,350 195,320 195,250 C195,170 128,130 128,80 L128,56 Z" fill="url(#glass-rose)"/>
      <g clip-path="url(#clip-rose)" role="img" aria-label="Snow-capped mountain range">
        <rect x="0" y="320" width="200" height="150" fill="url(#peak-rose)"/>
      </g>
    </svg>
    <div class="bottle__label brand-name">Tolmira</div>
    <div class="bottle__label brand-tag">SPARKLING WATER</div>
    <h2 class="bottle__label headline">SPARKLING<br>WATER</h2>
    <div class="bottle__label origin">Caucasian Mountains</div>
    <div class="bottle__label volume">16.9 fl oz (500 ml)</div>
  </article>

  <article class="bottle bottle--violet">
    <svg class="bottle__shape" viewBox="0 0 200 790">
      <defs>
        <linearGradient id="glass-violet" x1="0" y1="0" x2="0" y2="1">
          <stop offset="0" style="stop-color:var(--tint)"/>
          <stop offset=".35" style="stop-color:var(--tint);stop-opacity:.35"/>
          <stop offset=".62" style="stop-color:var(--glass)"/>
          <stop offset=".85" style="stop-color:var(--tint);stop-opacity:.3"/>
          <stop offset="1" style="stop-color:var(--tint)"/>
        </linearGradient>
        <linearGradient id="peak-violet" x1="0" y1="0" x2="0" y2="1">
          <stop offset="0" style="stop-color:var(--tint);stop-opacity:0"/>
          <stop offset=".5" style="stop-color:var(--tint);stop-opacity:.8"/>
          <stop offset="1" style="stop-color:var(--tint);stop-opacity:.15"/>
        </linearGradient>
        <clipPath id="clip-violet"><path d="M72,56 L72,80 C72,130 5,170 5,250 C5,320 22,350 22,400 C22,440 10,450 10,480 L10,730 C10,760 20,790 40,790 L160,790 C180,790 190,760 190,730 L190,480 C190,450 178,440 178,400 C178,350 195,320 195,250 C195,170 128,130 128,80 L128,56 Z"/></clipPath>
      </defs>
      <rect x="68" y="0" width="64" height="48" rx="5" style="fill:var(--tint)"/>
      <rect x="60" y="48" width="80" height="7" rx="3" style="fill:var(--tint)"/>
      <path d="M72,56 L72,80 C72,130 5,170 5,250 C5,320 22,350 22,400 C22,440 10,450 10,480 L10,730 C10,760 20,790 40,790 L160,790 C180,790 190,760 190,730 L190,480 C190,450 178,440 178,400 C178,350 195,320 195,250 C195,170 128,130 128,80 L128,56 Z" fill="url(#glass-violet)"/>
      <g clip-path="url(#clip-violet)" role="img" aria-label="Snow-capped mountain range">
        <rect x="0" y="320" width="200" height="150" fill="url(#peak-violet)"/>
      </g>
    </svg>
    <div class="bottle__label brand-name">Tolmira</div>
    <div class="bottle__label brand-tag">SPARKLING WATER</div>
    <h2 class="bottle__label headline">SPARKLING<br>WATER</h2>
    <div class="bottle__label origin">Caucasian Mountains</div>
    <div class="bottle__label volume">16.9 fl oz (500 ml)</div>
  </article>

  <article class="bottle bottle--azure">
    <svg class="bottle__shape" viewBox="0 0 200 790">
      <defs>
        <linearGradient id="glass-azure" x1="0" y1="0" x2="0" y2="1">
          <stop offset="0" style="stop-color:var(--tint)"/>
          <stop offset=".35" style="stop-color:var(--tint);stop-opacity:.35"/>
          <stop offset=".62" style="stop-color:var(--glass)"/>
          <stop offset=".85" style="stop-color:var(--tint);stop-opacity:.3"/>
          <stop offset="1" style="stop-color:var(--tint)"/>
        </linearGradient>
        <linearGradient id="peak-azure" x1="0" y1="0" x2="0" y2="1">
          <stop offset="0" style="stop-color:var(--tint);stop-opacity:0"/>
          <stop offset=".5" style="stop-color:var(--tint);stop-opacity:.8"/>
          <stop offset="1" style="stop-color:var(--tint);stop-opacity:.15"/>
        </linearGradient>
        <clipPath id="clip-azure"><path d="M72,56 L72,80 C72,130 5,170 5,250 C5,320 22,350 22,400 C22,440 10,450 10,480 L10,730 C10,760 20,790 40,790 L160,790 C180,790 190,760 190,730 L190,480 C190,450 178,440 178,400 C178,350 195,320 195,250 C195,170 128,130 128,80 L128,56 Z"/></clipPath>
      </defs>
      <rect x="68" y="0" width="64" height="48" rx="5" style="fill:var(--tint)"/>
      <rect x="60" y="48" width="80" height="7" rx="3" style="fill:var(--tint)"/>
      <path d="M72,56 L72,80 C72,130 5,170 5,250 C5,320 22,350 22,400 C22,440 10,450 10,480 L10,730 C10,760 20,790 40,790 L160,790 C180,790 190,760 190,730 L190,480 C190,450 178,440 178,400 C178,350 195,320 195,250 C195,170 128,130 128,80 L128,56 Z" fill="url(#glass-azure)"/>
      <g clip-path="url(#clip-azure)" role="img" aria-label="Snow-capped mountain range">
        <rect x="0" y="320" width="200" height="150" fill="url(#peak-azure)"/>
      </g>
    </svg>
    <div class="bottle__label brand-name">Tolmira</div>
    <div class="bottle__label brand-tag">SPARKLING WATER</div>
    <h2 class="bottle__label headline">SPARKLING<br>WATER</h2>
    <div class="bottle__label origin">Caucasian Mountains</div>
    <div class="bottle__label volume">16.9 fl oz (500 ml)</div>
  </article>

</main>
</body>
</html>
```